Review/Re-Design Supermarket E-Commerce website

We have launched our Supermarket E-commerce Website but feel it is lacking a modern feel.

Please re-design the current Supermarket E-commerce site, creating a more modern look and feel.

I am looking for design changes to things such as:

- Fonts
- Button shape & Size
- Shapes of boxes
- Layout of drop down menus
- A new shopping cart / button
- The Header (and in particular the use and positioning of the logo)
- Supplying a generic background image (currently berries)

Please do not change the structure of the page. For instance, the category selection will always be on the left, the items will always be displayed in rows of 3 and the shopping cart should be on the right.
Updates

Current site can be found at www.brovanmarket.com.au

Project Deadline Extended
Reason: designs coming in are generally too different from current design. we are looking for less that 10% change to the overall look and feel. one aspect that needs a lot of work is the checkout cart on the right hand side. please checkout http://www2.pelkinfreshmart.com.au/?gclid=QXRP4kdmwnLBHTYEzJuaPGEKtB

Target Market(s)

Consumers buying their weekly grocery shopping online

Industry/Entity Type

Shopping

Number of Pages Required

1 page

Requirements
Must have
• Stick to the branding of the Logo. Which is Red, Blue and White.
• Other colours may be used in small percentages.
Should not have
• Do not change the Structure of the site.

```html
<!DOCTYPE html>
<html lang="en">
<head>
<meta charset="utf-8">
<title>Brovan Market – Apples</title>
<link href="https://fonts.googleapis.com/css2?family=Open+Sans:ital,wght@0,400;0,600;0,700;1,400;1,700&display=swap" rel="stylesheet">
<style>
:root{
  --ink:#333a40;
  --ink-soft:#5d6369;
  --muted:#9aa0a6;
  --line:#e3e5e7;
  --header-bg:#f3f4f5;
  --panel:#ffffff;
  --green:#8db552;
  --green-dark:#79a13f;
  --brand-blue:#1f4f9c;
  --brand-red:#d8262b;
  --field:#e4e6e8;
  --page-dark:#1d1f22;
}
*{box-sizing:border-box;margin:0;padding:0}
html,body{width:1200px;height:900px;overflow:hidden}
body{font-family:"Open Sans",Arial,sans-serif;color:var(--ink);position:relative;background:var(--page-dark)}
.backdrop-left,.backdrop-right{position:absolute;top:0;height:900px}
.backdrop-left{left:0;width:170px;background:linear-gradient(180deg,#6b4a2a 0%,#8a5a32 18%,#5e6b3a 32%,#7b6a55 48%,#4a4238 62%,#2a2a2b 75%,var(--page-dark) 100%)}
.backdrop-right{right:0;width:169px;background:linear-gradient(180deg,#9a7650 0%,#b48a5e 20%,#8f6a4c 38%,#7a5440 52%,#4b3a31 66%,#2a2627 78%,var(--page-dark) 100%)}
.page{position:absolute;left:170px;top:0;width:861px;height:900px;background:var(--panel)}
.site-header{position:absolute;left:0;top:0;width:861px;height:157px;background:var(--header-bg);border-bottom:1px solid #dcdfe2}
.brand{position:absolute;left:56px;top:36px;display:flex;align-items:center;gap:10px;font-size:26px;font-weight:700;color:var(--brand-blue);letter-spacing:.5px}
.brand-dot{width:16px;height:16px;border-radius:50%;background:var(--brand-red)}
.main-nav{position:absolute;right:51px;top:40px;display:flex;align-items:center;gap:22px;font-size:11px;color:var(--ink)}
.btn-register{border:1px solid var(--green);border-radius:3px;padding:4px 10px;color:var(--ink)}
.support-label{position:absolute;left:58px;top:100px;font-size:8px;color:var(--muted)}
.support-phone{position:absolute;left:56px;top:114px;width:123px;height:26px;background:var(--field);border-radius:3px;display:flex;align-items:center;padding-left:10px;gap:10px;font-size:12px;font-weight:600;color:#6a7075}
.search{position:absolute;left:211px;top:114px;width:477px;height:26px;border:1px solid #cfd3d6;border-radius:3px;background:#fff;display:flex;overflow:hidden}
.search-scope{width:42px;background:#eceeef;border-right:1px solid #d6d9dc;font-size:10px;display:flex;align-items:center;justify-content:center;color:var(--ink-soft)}
.search-input{flex:1;font-size:10px;color:var(--ink-soft);display:flex;align-items:center;padding-left:13px}
.search-btn{width:26px;background:#a9aeb3;display:flex;align-items:center;justify-content:center}
.promo{position:absolute;left:708px;top:108px;display:flex;align-items:center;gap:4px}
.promo-art{width:40px;height:38px;border-radius:4px;background:linear-gradient(160deg,#6fa23a,#b3452a 55%,#8a5a2c)}
.promo-text{color:var(--brand-red);line-height:1;padding-top:6px}
.promo-text b{display:block;font-size:12px;font-weight:700}
.promo-text i{font-size:9px}

.sidebar{position:absolute;left:27px;top:197px;width:159px;height:703px;border-right:1px solid var(--line)}
.quick{list-style:none;padding-bottom:16px;border-bottom:1px solid var(--line);width:158px}
.quick li{display:flex;align-items:center;height:32px;font-size:11px;font-weight:700;gap:10px;padding-left:3px}
.quick small{margin-left:auto;font-size:6px;font-style:italic;font-weight:400;color:var(--muted);padding-right:14px}
.categories{list-style:none;width:158px;padding-top:4px}
.categories>li{height:29.5px;display:flex;align-items:center;justify-content:space-between;padding:0 12px 0 6px;font-size:10px;border-bottom:1px solid var(--line)}
.categories>li.open{border-bottom:none}
.subcategories{list-style:none}
.subcategories li{height:29.2px;display:flex;align-items:center;padding-left:26px;font-size:9.5px;color:var(--ink)}
.subcategories li.active{color:var(--muted);font-weight:700}

.breadcrumb{position:absolute;left:211px;top:195px;font-size:9.5px;color:var(--muted)}
.breadcrumb b{font-weight:400;color:var(--ink)}
.sort{position:absolute;left:588px;top:195px;font-size:9.5px;color:var(--ink)}
.sort span{color:var(--muted)}

.products{position:absolute;left:211px;top:221px;display:grid;grid-template-columns:repeat(3,144px);column-gap:23px;row-gap:17px}
.product{position:relative;height:198px;border:1px solid #dfe2e5;border-radius:3px;background:#fff;text-align:center}
.product-img{position:absolute;left:37px;top:18px;width:70px;height:80px;border-radius:40%}
.img-red{background:radial-gradient(circle at 40% 40%,#e8333c,#a3111b)}
.img-fuji{background:radial-gradient(circle at 40% 40%,#d9765a,#8c2a22)}
.img-pink{background:radial-gradient(circle at 40% 40%,#e23a52,#9c1024)}
.img-green{background:radial-gradient(circle at 40% 40%,#9be04a,#3f9a1c)}
.img-gala{background:radial-gradient(circle at 40% 40%,#f0b04a,#b8341e)}
.img-yellowbag{background:radial-gradient(circle at 40% 40%,#e4ea7a,#a6b82e)}
.img-yellow{background:radial-gradient(circle at 40% 40%,#f6d56a,#d99a2a)}
.product-name{position:absolute;left:0;right:0;top:114px;font-size:9.5px;line-height:14.5px;color:var(--ink-soft)}
.price{position:absolute;left:14px;top:162px;text-align:left;font-size:12.5px;font-weight:700;color:var(--ink);line-height:14px}
.price small{display:block;font-size:8px;font-style:italic;font-weight:400;color:var(--muted);line-height:10px}
.btn-add{position:absolute;right:10px;top:163px;width:45px;height:23px;border:1px solid #b9c1c8;border-radius:3px;font-size:9.5px;color:var(--ink-soft);display:flex;align-items:center;justify-content:center;background:#fff}
.btn-add.on{background:var(--green);border-color:var(--green);color:#fff;font-weight:600}
.qty{position:absolute;right:59px;top:163px;display:flex;align-items:center;gap:3px;font-size:8px;color:var(--ink-soft)}
.qty-step{width:13px;height:23px;border:1px solid #b9c1c8;border-radius:2px;display:flex;flex-direction:column;font-size:8px;line-height:11px}
.qty-step span{flex:1}
.qty-step span+span{border-top:1px solid #b9c1c8}
.mark{position:absolute;right:8px;top:6px}

.cart{position:absolute;left:715px;top:222px;width:160px;height:285px;background:#f7f8f8;border:1px solid #dcdfe2;box-shadow:0 1px 4px rgba(0,0,0,.12)}
.cart-head{height:32px;background:var(--green);color:#fff;display:flex;align-items:center;gap:8px;padding-left:14px;font-size:10px;margin:-1px -1px 0}
.cart-item{height:52px;border-bottom:1px solid var(--line);display:flex;justify-content:space-between;padding:11px 14px 0 15px;font-size:9.5px;line-height:14px;color:var(--ink-soft)}
.cart-item .amount{text-align:right;font-weight:700;font-size:11px;color:var(--ink)}
.cart-item small{display:block;font-size:6.5px;font-weight:400;color:var(--muted);line-height:8px}
.cart-total{padding:17px 14px 0 0;text-align:right;font-size:10px;color:var(--ink-soft)}
.cart-total b{font-size:13px;color:var(--ink);margin-left:4px}
.cart-actions{display:flex;gap:8px;padding:16px 0 0 14px}
.btn-open{width:62px;height:27px;border:1px solid #b9c1c8;border-radius:3px;font-size:9.5px;display:flex;align-items:center;justify-content:center;background:#fff}
.btn-checkout{width:66px;height:27px;border-radius:3px;background:var(--green);color:#fff;font-size:9.5px;font-weight:600;display:flex;align-items:center;justify-content:center}
.service{position:absolute;left:730px;display:flex;gap:9px;color:var(--ink-soft)}
.service b{font-weight:400;font-size:11px;display:block;line-height:13px}
.service small{font-size:6px;color:var(--muted);display:block;line-height:7px}
</style>
</head>
<body>
<div class="backdrop-left" role="img" aria-label="Background photo of fresh vegetables, fruit and dairy"></div>
<div class="backdrop-right" role="img" aria-label="Background photo of breads, pasta and cured meats"></div>

<main class="page">
  <header class="site-header">
    <div class="brand"><span class="brand-dot"></span>Brovan Market</div>
    <nav class="main-nav">
      <span>Products</span><span>My Cart</span><span>Login</span><span class="btn-register">Register</span>
    </nav>
    <div class="support-label">Call for support.</div>
    <div class="support-phone">
      <svg width="14" height="14" viewBox="0 0 24 24"><path fill="#9aa0a6" d="M6.6 10.8a15 15 0 0 0 6.6 6.6l2.2-2.2a1 1 0 0 1 1-.25 11 11 0 0 0 3.6.6 1 1 0 0 1 1 1V20a1 1 0 0 1-1 1A17 17 0 0 1 3 4a1 1 0 0 1 1-1h3.5a1 1 0 0 1 1 1 11 11 0 0 0 .6 3.6 1 1 0 0 1-.25 1z"/></svg>
      1300 555 019
    </div>
    <div class="search">
      <div class="search-scope">All ⌄</div>
      <div class="search-input">Search...</div>
      <div class="search-btn"><svg width="12" height="12" viewBox="0 0 24 24"><circle cx="10" cy="10" r="6.5" fill="none" stroke="#fff" stroke-width="2.5"/><path d="M15 15l6 6" stroke="#fff" stroke-width="2.5"/></svg></div>
    </div>
    <div class="promo">
      <div class="promo-art" role="img" aria-label="Basket filled with groceries"></div>
      <div class="promo-text"><b>Get Free</b><i>Grocerie Basket</i></div>
    </div>
  </header>

  <aside class="sidebar">
    <ul class="quick">
      <li><svg width="20" height="20" viewBox="0 0 24 24"><path fill="#f2b01e" d="M12 2l3 6.6 7.2.7-5.4 4.8 1.6 7.1L12 17.5 5.6 21.2l1.6-7.1L1.8 9.3 9 8.6z"/></svg>Favorites<small>58 products</small></li>
      <li><svg width="20" height="20" viewBox="0 0 24 24"><path fill="#e0403a" d="M3 12l9-9h8v8l-9 9z"/><circle cx="16" cy="7" r="1.8" fill="#fff"/></svg>Online Specials</li>
    </ul>
    <ul class="categories">
      <li>Fruit<svg width="5" height="7"><path d="M0 0l5 3.5L0 7z" fill="#c8ccd0"/></svg></li>
      <li>Meat<svg width="5" height="7"><path d="M0 0l5 3.5L0 7z" fill="#c8ccd0"/></svg></li>
      <li>Serviced Deli<svg width="5" height="7"><path d="M0 0l5 3.5L0 7z" fill="#c8ccd0"/></svg></li>
      <li class="open">Bakery<svg width="7" height="5"><path d="M0 0h7L3.5 5z" fill="#555"/></svg></li>
    </ul>
    <ul class="subcategories">
      <li>Biscuits &amp; Cookies</li>
      <li class="active">Bread Rolls Pack</li>
      <li>Bread Rolls Single</li>
      <li>Cakes</li>
      <li>Croissants</li>
      <li>Crumpets</li>
      <li>Fruit Buns &amp; Cakes</li>
      <li>Grain Bread</li>
      <li>Muffin Cakes</li>
      <li>Muffins</li>
      <li>Pikelets &amp; Pancakes</li>
      <li>Pizza Bases &amp; Pita Bread</li>
      <li>Raisin Toast</li>
      <li>Rye Bread</li>
      <li>Savoury Packets</li>
      <li>Snacks</li>
      <li>Sourdough Bread</li>
    </ul>
  </aside>

  <div class="breadcrumb">Home &nbsp;/&nbsp; Fruit &nbsp;/&nbsp; <b>Apples</b></div>
  <div class="sort">Sort by: <span>Alphabetical ⌄</span></div>

  <section class="products">
    <article class="product">
      <svg class="mark" width="12" height="10" viewBox="0 0 12 10"><path d="M1 5l3.5 3.5L11 1" fill="none" stroke="#8db552" stroke-width="1.8"/></svg>
      <div class="product-img img-red" role="img" aria-label="Bag of red apples"></div>
      <div class="product-name">Apples Red<br>2kg Bag</div>
      <div class="price">$16,78<small>$16,78ea</small></div>
      <div class="qty">2<div class="qty-step"><span>+</span><span>−</span></div></div>
      <div class="btn-add">Add</div>
    </article>
    <article class="product">
      <div class="product-img img-fuji" role="img" aria-label="Fuji apple"></div>
      <div class="product-name">Fuji Apples<br>Each</div>
      <div class="price">$0,60<small>$0,60ea</small></div>
      <div class="btn-add">Add</div>
    </article>
    <article class="product">
      <div class="product-img img-pink" role="img" aria-label="Rosy Blush apple"></div>
      <div class="product-name">Rosy Blush Apples<br>Each</div>
      <div class="price">$0,60<small>$0,60ea</small></div>
      <div class="btn-add">Add</div>
    </article>
    <article class="product">
      <svg class="mark" width="13" height="13" viewBox="0 0 13 13"><circle cx="6.5" cy="6.5" r="6" fill="#e0403a"/><path d="M4.3 4.3l4.4 4.4M8.7 4.3l-4.4 4.4" stroke="#fff" stroke-width="1.5"/></svg>
      <div class="product-img img-green" role="img" aria-label="Green apple"></div>
      <div class="product-name">Green Apples<br>Each</div>
      <div class="price">$0,60<small>$0,60ea</small></div>
      <div class="btn-add">Add</div>
    </article>
    <article class="product">
      <div class="product-img img-gala" role="img" aria-label="Royal Gala apple"></div>
      <div class="product-name">Royal Gala Apples<br>Each</div>
      <div class="price">$0,60<small>$0,60ea</small></div>
      <div class="qty">1<div class="qty-step"><span>+</span><span>−</span></div></div>
      <div class="btn-add on">Add</div>
    </article>
    <article class="product">
      <svg class="mark" width="12" height="10" viewBox="0 0 12 10"><path d="M1 5l3.5 3.5L11 1" fill="none" stroke="#8db552" stroke-width="1.8"/></svg>
      <div class="product-img img-yellowbag" role="img" aria-label="Bag of yellow apples"></div>
      <div class="product-name">Yellow Apples 1.5kg<br>Bag</div>
      <div class="price">$5.20<small>$5,20ea</small></div>
      <div class="btn-add">Add</div>
    </article>
    <article class="product">
      <div class="product-img img-yellow" role="img" aria-label="Yellow apple"></div>
      <div class="product-name">Yellow Apples<br>Each</div>
      <div class="price">$0,60<small>$0,60ea</small></div>
      <div class="btn-add">Add</div>
    </article>
  </section>

  <aside class="cart">
    <div class="cart-head">
      <svg width="16" height="14" viewBox="0 0 24 20"><path d="M1 2h4l3 11h12l3-8H7" fill="none" stroke="#fff" stroke-width="2"/><circle cx="10" cy="17" r="1.8" fill="#fff"/><circle cx="18" cy="17" r="1.8" fill="#fff"/></svg>
      3 Items in your cart
    </div>
    <div class="cart-item"><span>Apples Red<br>2kg Bag</span><span class="amount">$16,78<small>quantity: 2</small></span></div>
    <div class="cart-item"><span>Green Apples<br>Each</span><span class="amount">$3,00<small>quantity: 5</small></span></div>
    <div class="cart-item"><span>Yellow Apples 1.5kg<br>Bag</span><span class="amount" style="padding-top:7px">$5,20</span></div>
    <div class="cart-total">Subtotal: <b>$24,98</b></div>
    <div class="cart-actions"><div class="btn-open">Open Cart</div><div class="btn-checkout">Checkout</div></div>
  </aside>

  <div class="service" style="top:517px">
    <svg width="24" height="24" viewBox="0 0 24 24"><path d="M4 8h16l-1.5 14h-13z" fill="#7f8c98"/><path d="M8 8V5a4 4 0 0 1 8 0v3" fill="none" stroke="#7f8c98" stroke-width="2"/></svg>
    <div><b>Click&amp;Collect</b><small>4/12-18 Marlow Street</small><small>Brovan TAS 7300</small></div>
  </div>
  <div class="service" style="top:555px">
    <svg width="24" height="20" viewBox="0 0 24 20"><path d="M1 4h13v10H1zM14 8h5l4 4v2h-9z" fill="#7f8c98"/><circle cx="5" cy="16" r="2.5" fill="#7f8c98"/><circle cx="18" cy="16" r="2.5" fill="#7f8c98"/></svg>
    <div><b>Deivery Info</b></div>
  </div>
</main>
</body>
</html>
```